Book cover for my book "Amber Orchard Letters"

Simple graphic with the title "Amber Orchard Letters" for a book I am self publishing. This book teaches people how to divorce with kindness and compassion without compromising their legal rights and getting what is fair. I am a lawyer telling them everything on how to hire a lawyer, what process to choose, how to build a support system, how to keep the kids out of it. It should exude authority, but also kindness and compassion. It's real legal information but from a lens that doesn't give a bunch of money to lawyers to burn down your family.

Target Market(s)

People seeking to divorce but don't want to spend a bunch of money or destroy their spouse

Industry/Entity Type

Legal

Requirements
Must have
• Dignity
Nice to have
• Envision two people parting, moving away from each other but something that is altruistic popping up between them? I'm not artist. Keep in mind "couple" is generic so not gender specific.
Should not have
• Trite things like a handshake,

```html
<!DOCTYPE html>
<html lang="en">
<head>
<meta charset="utf-8">
<title>Amber Orchard Letters – Book Cover</title>
<link rel="stylesheet" href="https://fonts.googleapis.com/css2?family=Cinzel:wght@400;500&display=swap">
<style>
  :root {
    --backdrop: #dadada;
    --paper: #efeeec;
    --ink: #1c1c1c;
    --wine: #7d1a1c;
    --muted: #6d6d6d;
    --art-ink: #3a3a3a;
    --art-mid: #b9b8b6;
    --art-wine: #8a2a2c;
  }
  html, body {
    margin: 0;
    padding: 0;
    width: 1200px;
    height: 1085px;
    overflow: hidden;
    background: var(--backdrop);
  }
  .cover {
    position: absolute;
    left: 246px;
    top: 42px;
    width: 708px;
    height: 1000px;
    background: var(--paper);
    font-family: "Cinzel", "Times New Roman", serif;
    text-align: center;
    overflow: hidden;
  }
  .title {
    position: absolute;
    top: 62px;
    left: 0;
    right: 0;
    margin: 0;
    font-weight: 400;
    line-height: 1;
    text-transform: uppercase;
  }
  .title-line {
    display: block;
    white-space: nowrap;
  }
  .title-top {
    color: var(--ink);
    font-size: 54px;
    letter-spacing: 1px;
  }
  .title-main {
    color: var(--wine);
    font-size: 98px;
    margin-top: 2px;
    letter-spacing: 1px;
  }
  .artwork {
    position: absolute;
    left: 50px;
    top: 215px;
    width: 606px;
    height: 600px;
    border-radius: 40%;
    background:
      linear-gradient(90deg,
        rgba(239,238,236,0) 0%, rgba(239,238,236,0) 100%),
      linear-gradient(90deg,
        var(--art-ink) 8%, var(--art-mid) 38%, #8d8d8d 50%,
        var(--art-mid) 62%, var(--art-wine) 92%);
    opacity: 0.55;
    filter: blur(18px);
  }
  .publisher {
    position: absolute;
    top: 866px;
    left: 0;
    right: 0;
    display: flex;
    align-items: center;
    justify-content: center;
    gap: 10px;
  }
  .publisher-dot {
    width: 14px;
    height: 14px;
    border-radius: 50%;
    background: var(--wine);
  }
  .publisher-name {
    color: var(--wine);
    font-size: 22px;
    font-weight: 500;
    letter-spacing: 1px;
    white-space: nowrap;
  }
  .tagline {
    position: absolute;
    top: 932px;
    left: 0;
    right: 0;
    margin: 0;
    color: var(--muted);
    font-size: 15px;
    line-height: 1.35;
    letter-spacing: 1px;
  }
</style>
</head>
<body>
  <main class="cover">
    <h1 class="title">
      <span class="title-line title-top">Amber Orchard</span>
      <span class="title-line title-main">Letters</span>
    </h1>

    <div class="artwork" role="img"
         aria-label="Two fragmented walking figures, one black and one dark red, moving apart from a central scale of justice surrounded by radiating grey lines"></div>

    <div class="publisher">
      <span class="publisher-dot"></span>
      <span class="publisher-name">The Kindred Counsel</span>
    </div>

    <p class="tagline">A LAWYER TELLING YOU<br>THE COMPASSIONATE PROCESS OF DIVORCE</p>
  </main>
</body>
</html>
```